Small Business coaching and services company

Need a powerpoint template design for a company that provides Human Resources services as well sales and business coaching.

```html
<!DOCTYPE html>
<html lang="en"><head><meta charset="utf-8"><title>BrightPath Presentation Template</title>
<link href="https://fonts.googleapis.com/css2?family=Poppins:wght@400;500;600;700&display=swap" rel="stylesheet">
<style>
:root{--purple:#6a2c9c;--purple2:#8a55c0;--yellow:#f6ad00;--dark:#1c1c1e;--ink:#222;--grey:#9a9a9a;--line:#e6e6e6;--paper:#fff}
*{box-sizing:border-box;margin:0;padding:0}
html,body{width:1200px;height:866px;overflow:hidden;background:#fff;font-family:'Poppins',sans-serif;color:var(--ink)}
.slide{position:absolute;width:178px;height:98px;background:var(--paper);box-shadow:0 3px 9px rgba(0,0,0,.13);overflow:hidden}
.c1{left:29px}.c2{left:222px}.c3{left:414px}.c4{left:607px}.c5{left:800px}.c6{left:993px}
.r1{top:37px}.r2{top:154px}.r3{top:268px}.r4{top:383px}.r5{top:498px}.r6{top:614px}.r7{top:729px}
.abs{position:absolute}
.foot{position:absolute;left:0;right:0;bottom:0;height:5px;background:var(--yellow);font-size:2.3px;color:#fff;display:flex;justify-content:space-between;align-items:center;padding:0 5px}
.foot i{position:absolute;left:84px;bottom:1px;width:9px;height:9px;border-radius:50%;background:#fff;border:1.2px solid var(--purple)}
.title{position:absolute;top:9px;left:0;right:0;text-align:center;font-size:6px;font-weight:600;color:var(--ink)}
.title b,.t b{color:var(--purple);font-weight:600}
.title::before{content:"";display:block;width:8px;height:1px;background:var(--yellow);margin:0 auto 1px}
.sub{position:absolute;top:19px;left:0;right:0;text-align:center;font-size:1.8px;color:var(--grey)}
.t{position:absolute;font-size:6px;font-weight:600}
.tiny{font-size:1.9px;line-height:2.6px;color:var(--grey)}
.lbl{font-size:2.4px;font-weight:600;color:var(--ink)}
.brand{font-size:6px;font-weight:600;color:var(--yellow);display:flex;align-items:center;gap:2px}
.brand::before{content:"";width:6px;height:6px;border-radius:50%;background:var(--purple2)}
.dark{background:var(--dark);color:#fff}
.ph{position:absolute}
.card{position:absolute;background:#fff;box-shadow:0 1px 3px rgba(0,0,0,.12)}
.pcirc{position:absolute;border-radius:50%;background:linear-gradient(#c9b8a6,#7d6a5c)}
.icons{position:absolute;inset:8px 8px}
</style></head><body>

<!-- Row 1 -->
<section class="slide dark c1 r1">
 <div class="ph" role="img" aria-label="Dimmed office desk photograph" style="inset:0;background:linear-gradient(135deg,#2a2a2c,#151516)"></div>
 <div class="abs brand" style="left:62px;top:30px">BrightPath</div>
 <div class="abs" style="left:0;right:0;top:44px;text-align:center;font-size:5.2px;font-weight:600">Presentation Tittle Goes Here</div>
 <div class="abs" style="left:0;right:0;top:52px;text-align:center;font-size:2.4px;color:#bbb">Credential Subtitle Presentation</div>
 <div class="abs" style="left:0;right:0;top:68px;text-align:center;font-size:2.8px;font-weight:600">Mr. Daniel <span style="color:var(--yellow)">Hart</span></div>
 <div class="abs" style="left:8px;top:90px;font-size:2.2px">February 2023</div><div class="abs" style="right:8px;top:90px;font-size:2.2px">website.com</div>
</section>
<section class="slide dark c2 r1">
 <div class="ph" role="img" aria-label="Dimmed office desk photograph" style="inset:0;background:linear-gradient(135deg,#2a2a2c,#151516)"></div>
 <div class="ph" role="img" aria-label="Large silver growth chart graphic" style="left:105px;top:18px;width:62px;height:60px;border-radius:50%;background:radial-gradient(circle,#e8e8e8,#777 60%,transparent 70%)"></div>
 <div class="abs brand" style="left:15px;top:30px">BrightPath</div>
 <div class="abs" style="left:15px;top:44px;font-size:5.2px;font-weight:600">Presentation Tittle Goes Here</div>
 <div class="abs" style="left:15px;top:52px;font-size:2.4px;color:#bbb">Credential Subtitle Presentation</div>
 <div class="abs" style="left:15px;top:68px;font-size:2.8px;font-weight:600">Mr. Daniel <span style="color:var(--yellow)">Hart</span></div>
 <div class="abs" style="left:8px;top:90px;font-size:2.2px">February 2023</div><div class="abs" style="right:8px;top:90px;font-size:2.2px">website.com</div>
</section>
<section class="slide dark c3 r1">
 <div class="ph" role="img" aria-label="Dimmed office desk photograph" style="inset:0;background:linear-gradient(135deg,#2a2a2c,#151516)"></div>
 <div class="ph" role="img" aria-label="Large bronze growth chart graphic" style="left:105px;top:18px;width:62px;height:60px;border-radius:50%;background:radial-gradient(circle,#d9b08c,#6b4a34 60%,transparent 70%)"></div>
 <div class="abs brand" style="left:15px;top:30px">BrightPath</div>
 <div class="abs" style="left:15px;top:44px;font-size:5.2px;font-weight:600">Presentation Tittle Goes Here</div>
 <div class="abs" style="left:15px;top:52px;font-size:2.4px;color:#bbb">Credential Subtitle Presentation</div>
 <div class="abs" style="left:15px;top:68px;font-size:2.8px;font-weight:600;color:var(--purple2)">Mr. Daniel <span style="color:var(--yellow)">Hart</span></div>
 <div class="abs" style="left:8px;top:90px;font-size:2.2px">February 2023</div><div class="abs" style="right:8px;top:90px;font-size:2.2px">website.com</div>
</section>
<section class="slide c4 r1">
 <div class="ph" role="img" aria-label="Faint growth chart graphic" style="left:100px;top:15px;width:65px;height:62px;border-radius:50%;background:radial-gradient(circle,#f2f2f2,#fafafa 60%,transparent 70%)"></div>
 <div class="abs brand" style="left:15px;top:30px">BrightPath</div>
 <div class="abs" style="left:15px;top:44px;font-size:5.2px;font-weight:600">Presentation Tittle Goes Here</div>
 <div class="abs" style="left:15px;top:52px;font-size:2.4px;color:var(--grey)">Credential Subtitle Presentation</div>
 <div class="abs" style="left:15px;top:68px;font-size:2.8px;font-weight:600;color:var(--purple)">Mr. Daniel <span style="color:var(--yellow)">Hart</span></div>
 <div class="abs" style="left:8px;top:90px;font-size:2.2px">February 2023</div><div class="abs" style="right:8px;top:90px;font-size:2.2px">website.com</div>
</section>
<section class="slide c5 r1">
 <div class="abs brand" style="left:60px;top:28px">BrightPath</div>
 <div class="abs" style="left:0;right:0;top:44px;text-align:center;font-size:5.2px;font-weight:600">Presentation Tittle Goes Here</div>
 <div class="abs" style="left:0;right:0;top:52px;text-align:center;font-size:2.4px;color:var(--grey)">Credential Subtitle Presentation</div>
 <div class="abs" style="left:0;right:0;top:68px;text-align:center;font-size:2.8px;font-weight:600">Mr. Daniel <span style="color:var(--yellow)">Hart</span></div>
 <div class="abs" style="left:8px;top:90px;font-size:2.2px">February 2023</div><div class="abs" style="right:8px;top:90px;font-size:2.2px">website.com</div>
</section>
<section class="slide c6 r1">
 <div class="title" style="top:8px">Presentation <b>List</b></div>
 <svg class="abs" style="left:22px;top:30px" width="136" height="44" font-size="2.2" font-family="Poppins" fill="#333">
  <g stroke="#ccc" stroke-width=".3"><line x1="0" y1="3" x2="52" y2="3"/><line x1="0" y1="16" x2="52" y2="16"/><line x1="0" y1="29" x2="52" y2="29"/><line x1="0" y1="41" x2="52" y2="41"/><line x1="78" y1="3" x2="132" y2="3"/><line x1="78" y1="16" x2="132" y2="16"/><line x1="78" y1="29" x2="132" y2="29"/><line x1="78" y1="41" x2="132" y2="41"/></g>
  <line x1="0" y1="16" x2="20" y2="16" stroke="#6a2c9c" stroke-width=".6"/>
  <text x="0" y="2">COVER SLIDES</text><text x="48" y="2">01</text><text x="0" y="15">PRESENTATION LIST</text><text x="48" y="15">03</text><text x="0" y="28">ABOUT US</text><text x="48" y="28">04</text><text x="0" y="40">OUR MISSIONS &amp; VISION</text><text x="48" y="40">06</text>
  <text x="78" y="2">INFOGRAPH ONE</text><text x="128" y="2">07</text><text x="78" y="15">INFOGRAPH TWO</text><text x="128" y="15">08</text><text x="78" y="28">INFOGRAPH THREE</text><text x="128" y="28">09</text><text x="78" y="40">CLOSING SLIDES</text><text x="128" y="40">10</text>
 </svg>
 <div class="foot"><span>website.com</span><i></i><span>Page | 6</span></div>
</section>

<!-- Row 2 -->
<section class="slide c1 r2">
 <div class="title">Our <b>Vision</b></div><div class="sub">Here Our Credential Subtitle</div>
 <div class="abs" style="left:22px;top:27px;width:134px;height:47px;background:var(--purple);box-shadow:0 2px 4px rgba(0,0,0,.2);color:#fff;font-size:3.3px;font-style:italic;text-align:center;display:flex;align-items:center;padding:0 10px;line-height:5px">Lorem ipsum dolor sit amet, consectetuer adipiscing elit. Maecenas porttitor congue massa. Fusce posuere, magna sed pulvinar ultricies, purus lectus malesuada libero.</div>
 <div class="foot"><span>website.com</span><i></i><span>Page | 7</span></div>
</section>
<section class="slide c2 r2">
 <div class="title">Our <b>Mission</b></div>
 <div class="abs" style="left:10px;top:28px;width:158px;display:grid;grid-template-columns:repeat(3,1fr);row-gap:10px;column-gap:6px;text-align:center">
  <div><div class="lbl">Mission One</div><div class="tiny">Lorem ipsum dolor sit amet, consectetuer adipiscing elit.</div></div>
  <div class="card" style="position:relative"><div class="lbl">Mission Two</div><div class="tiny">Lorem ipsum dolor sit amet, consectetuer adipiscing elit.</div></div>
  <div><div class="lbl">Mission Three</div><div class="tiny">Lorem ipsum dolor sit amet, consectetuer adipiscing elit.</div></div>
  <div><div class="lbl">Mission Four</div><div class="tiny">Lorem ipsum dolor sit amet, consectetuer adipiscing elit.</div></div>
  <div><div class="lbl">Mission Five</div><div class="tiny">Lorem ipsum dolor sit amet, consectetuer adipiscing elit.</div></div>
  <div><div class="lbl">Mission Six</div><div class="tiny">Lorem ipsum dolor sit amet, consectetuer adipiscing elit.</div></div>
 </div>
 <div class="foot"><span>website.com</span><i></i><span>Page | 8</span></div>
</section>
<section class="slide c3 r2">
 <div class="ph" role="img" aria-label="Photo of two colleagues working outdoors" style="left:19px;top:24px;width:32px;height:42px;background:linear-gradient(135deg,#6f8a4a,#3d3a2c)"></div>
 <div class="t" style="left:80px;top:24px">Our <b>Legacy</b></div>
 <div class="abs tiny" style="left:80px;top:33px;width:80px">Lorem ipsum dolor sit amet, consectetuer adipiscing elit. Maecenas porttitor congue massa. Fusce posuere, magna sed pulvinar ultricies.</div>
 <div class="abs" style="left:80px;top:51px;display:flex;gap:2px;text-align:center">
  <div class="card" style="position:relative;width:13px;height:12px;font-size:3px;color:var(--yellow);font-weight:600">12+<div class="tiny" style="font-size:1.4px">Partnership</div></div>
  <div style="width:13px;height:12px;background:var(--purple);font-size:3px;color:#fff;font-weight:600">400+<div style="font-size:1.4px">Satisfy Cust</div></div>
  <div class="card" style="position:relative;width:13px;height:12px;font-size:3px;color:var(--yellow);font-weight:600">120+<div class="tiny" style="font-size:1.4px">Employee</div></div>
 </div>
 <div class="foot"><span>website.com</span><i></i><span>Page | 9</span></div>
</section>
<section class="slide c4 r2">
 <div class="title" style="top:8px">Our <b>Pictures</b></div><div class="sub" style="top:17px">Here Our Credential Subtitle</div>
 <div class="ph" role="img" aria-label="Photo of a coffee cup on a desk" style="left:12px;top:25px;width:41px;height:33px;background:linear-gradient(135deg,#9aa4a8,#4d5558)"></div>
 <div class="ph" role="img" aria-label="Photo of hands typing on a laptop" style="left:68px;top:25px;width:41px;height:33px;background:linear-gradient(135deg,#b9c3cc,#5f6f7a)"></div>
 <div class="ph" role="img" aria-label="Photo of a person with laptop in pink light" style="left:124px;top:25px;width:41px;height:33px;background:linear-gradient(135deg,#b34a6d,#2d2b4a)"></div>
 <div class="abs" style="left:12px;top:61px;width:153px;display:flex;justify-content:space-between;text-align:center">
  <div style="width:41px"><div class="lbl" style="font-size:2px">Picture One</div><div class="tiny" style="font-size:1.6px">Lorem ipsum dolor sit amet, consectetuer adipisc.</div></div>
  <div style="width:41px"><div class="lbl" style="font-size:2px">Picture Two</div><div class="tiny" style="font-size:1.6px">Lorem ipsum dolor sit amet, consectetuer adipisc.</div></div>
  <div style="width:41px"><div class="lbl" style="font-size:2px">Picture Three</div><div class="tiny" style="font-size:1.6px">Lorem ipsum dolor sit amet, consectetuer adipisc.</div></div>
 </div>
 <div class="foot"><span>website.com</span><i></i><span>Page | 10</span></div>
</section>
<section class="slide c5 r2">
 <div class="title" style="top:10px">Our <b>Company</b></div><div class="sub" style="top:19px">Here Our Credential Subtitle</div>
 <div class="abs tiny" style="left:25px;top:34px;width:128px;text-align:center"><span style="color:var(--yellow)">Lorem ipsum</span> dolor sit amet, consectetuer adipiscing elit. Maecenas porttitor congue massa. Fusce posuere, magna sed pulvinar ultricies, purus lectus malesuada libero, sit amet commodo magna eros quis urna.</div>
 <div class="abs" style="left:15px;top:62px;width:148px;display:flex;justify-content:space-between;text-align:center;font-size:4.2px;font-weight:500">
  <div>1092<div class="tiny">Project Done</div></div><div>1290<div class="tiny">Satisfy Costumer</div></div><div>45<div class="tiny">Global Partnership</div></div><div>23+<div class="tiny">Certifications Company</div></div>
 </div>
 <div class="foot"><span>website.com</span><i></i><span>Page | 11</span></div>
</section>
<section class="slide c6 r2">
 <div class="title" style="top:8px">Analyse <b>Chart</b></div>
 <div class="card" style="left:12px;top:25px;width:68px;height:56px"></div>
 <svg class="abs" style="left:14px;top:27px" width="64" height="52" font-size="2" font-family="Poppins" fill="#555">
  <text x="1" y="3" font-weight="600" fill="#222">Finding Chart</text>
  <text x="6" y="12">Data Five</text><rect x="22" y="10" width="8" height="2" fill="#6a2c9c"/>
  <text x="6" y="19">Data Four</text><rect x="22" y="17" width="11" height="2" fill="#777"/>
  <text x="6" y="26">Data Three</text><rect x="22" y="24" width="20" height="2" fill="#f6ad00"/>
  <text x="6" y="33">Data Two</text><rect x="22" y="31" width="22" height="2" fill="#6a2c9c"/>
  <text x="6" y="40">Data One</text><rect x="22" y="38" width="17" height="2" fill="#f6ad00"/>
  <text x="22" y="48">0</text><text x="33" y="48">100</text><text x="46" y="48">200</text>
 </svg>
 <div class="card" style="left:84px;top:25px;width:82px;height:56px;padding:3px 4px">
  <div class="lbl" style="font-size:2px">Analyse One:</div><div class="tiny" style="font-size:1.6px;line-height:2.1px">Lorem ipsum dolor sit amet, consectetuer adipiscing elit. Maecenas porttitor congue massa fusce.</div>
  <div class="lbl" style="font-size:2px;margin-top:2px">Analyse Two:</div><div class="tiny" style="font-size:1.6px;line-height:2.1px">Lorem ipsum dolor sit amet, consectetuer adipiscing elit. Maecenas porttitor congue massa fusce.</div>
  <div class="lbl" style="font-size:2px;margin-top:2px">Analyse Three:</div><div class="tiny" style="font-size:1.6px;line-height:2.1px">Lorem ipsum dolor sit amet, consectetuer adipiscing elit. Maecenas porttitor congue massa fusce.</div>
 </div>
 <div class="foot"><span>website.com</span><i></i><span>Page | 12</span></div>
</section>

<!-- Row 3 -->
<section class="slide c1 r3">
 <div class="t" style="left:64px;top:18px">S.W.O.T <b>Analayse</b></div>
 <div class="abs tiny" style="left:25px;top:31px;width:128px;text-align:center">Lorem ipsum dolor sit amet, consectetuer adipiscing elit. Maecenas porttitor congue massa. Fusce posuere, magna sed pulvinar ultricies.</div>
 <div class="abs" style="left:10px;top:49px;width:160px;display:flex;gap:2px">
  <div style="flex:1;padding:2px"><div class="lbl" style="font-weight:400">Strenght</div><div class="tiny" style="font-size:1.5px;line-height:2.2px">1. Business Enhancement Plan<br>2. Growth Strategy is one<br>3. Way to development it self<br>4. With Super team together</div></div>
  <div style="flex:1;padding:2px;background:var(--purple);color:#fff;height:28px"><div class="lbl" style="font-weight:400;color:#fff">Weakness</div><div style="font-size:1.5px;line-height:2.2px">1. Business Enhancement Plan<br>2. Growth Strategy is one<br>3. Way to development it self<br>4. With Super team together</div></div>
  <div style="flex:1;padding:2px"><div class="lbl" style="font-weight:400">Opportunity</div><div class="tiny" style="font-size:1.5px;line-height:2.2px">1. Ways to develop it self<br>2. Business Enhancement Plan<br>3. Growth Strategy is one<br>4. With Super team together</div></div>
  <div style="flex:1;padding:2px"><div class="lbl" style="font-weight:400">Thread</div><div class="tiny" style="font-size:1.5px;line-height:2.2px">1. Business Enhancement Plan<br>2. Growth Strategy is one<br>3. Ways to develop it self<br>4. With Super team together</div></div>
 </div>
 <div class="foot"><span>website.com</span><i></i><span>Page | 13</span></div>
</section>
<section class="slide c2 r3">
 <div class="ph" role="img" aria-label="Top-down photo of a laptop, coffee and notebook" style="left:10px;top:0;width:57px;height:76px;background:linear-gradient(135deg,#f1f1f1,#b9b9b9)"></div>
 <div class="t" style="left:89px;top:15px;color:var(--yellow)"><span style="color:var(--yellow)">Our</span> <b>Step</b></div>
 <div class="abs tiny" style="left:89px;top:23px;width:60px;font-size:1.6px;line-height:2.2px">Lorem ipsum dolor sit amet, consectetuer adipiscing elit. Maecenas porttitor congue massa.</div>
 <svg class="abs" style="left:55px;top:36px" width="40" height="40" fill="none" stroke="#6a2c9c" stroke-width=".5"><path d="M0 2H38M0 18H38M0 34H38"/></svg>
 <div class="abs" style="left:96px;top:35px;width:55px;font-size:1.8px"><div style="color:var(--purple);font-weight:600">First Step</div><div class="tiny" style="font-size:1.5px;line-height:2px">Lorem ipsum dolor sit amet, consectetuer adipisc.</div>
  <div style="color:var(--purple);font-weight:600;margin-top:8px">Second Step</div><div class="tiny" style="font-size:1.5px;line-height:2px">Lorem ipsum dolor sit amet, consectetuer adipisc.</div>
  <div style="color:var(--purple);font-weight:600;margin-top:8px">Third Step</div><div class="tiny" style="font-size:1.5px;line-height:2px">Lorem ipsum dolor sit amet, consectetuer adipisc.</div></div>
 <div class="foot"><span>website.com</span><i></i><span>Page | 14</span></div>
</section>
<section class="slide c3 r3">
 <div class="ph" role="img" aria-label="Photo of businessmen meeting in a bright office lounge" style="left:0;top:17px;width:93px;height:63px;background:linear-gradient(135deg,#a8b6c0,#3f4c58)"></div>
 <div class="t" style="left:98px;top:18px"><span style="color:var(--yellow)">Our</span> <b>Plan</b></div>
 <div class="abs tiny" style="left:98px;top:27px;width:68px;font-size:1.6px;line-height:2.2px">Lorem ipsum dolor sit amet, consectetuer adipiscing elit. Maecenas porttitor congue massa.</div>
 <div class="abs" style="left:98px;top:40px;width:66px;font-size:1.8px"><div style="font-weight:600">• First Plan</div><div class="tiny" style="font-size:1.5px;line-height:2.1px">- Lorem ipsum dolor sit amet, consectetuer.<br>- Lorem ipsum dolor sit amet, consectetuer.<br>- Lorem ipsum dolor sit amet, consectetuer.</div>
  <div style="font-weight:600;margin-top:3px">• Second Plan</div><div class="tiny" style="font-size:1.5px;line-height:2.1px">- Lorem ipsum dolor sit amet, consectetuer.<br>- Lorem ipsum dolor sit amet, consectetuer.<br>- Lorem ipsum dolor sit amet, consectetuer.</div></div>
 <div class="foot"><span>website.com</span><i></i><span>Page | 15</span></div>
</section>
<section class="slide c4 r3">
 <div class="ph" role="img" aria-label="Photo of stacked team hands" style="left:6px;top:9px;width:36px;height:36px;background:linear-gradient(135deg,#d6c2b0,#6f8c9e)"></div>
 <div class="abs tiny" style="left:45px;top:10px;width:28px;font-size:1.5px;line-height:2px">Lorem ipsum dolor sit amet, consectetuer adipiscing elit. Maecenas porttitor.</div>
 <div class="ph" role="img" aria-label="Photo of hands joined together" style="left:79px;top:9px;width:36px;height:36px;background:linear-gradient(135deg,#7a5a4a,#2f4a3a)"></div>
 <div class="ph" role="img" aria-label="Photo of a handshake" style="left:43px;top:47px;width:36px;height:36px;background:linear-gradient(135deg,#e4e6ea,#9aa2ac)"></div>
 <div class="abs tiny" style="left:6px;top:57px;width:34px;font-size:1.5px;line-height:2px">Lorem ipsum dolor sit amet, consectetuer adipiscing elit. Maecenas porttitor.</div>
 <div class="abs tiny" style="left:82px;top:57px;width:30px;font-size:1.5px;line-height:2px">Lorem ipsum dolor sit amet, consectetuer adipiscing elit. Maecenas porttitor.</div>
 <div class="abs" style="left:124px;top:41px;font-size:5px;font-weight:600">Portofolio</div>
 <div class="abs tiny" style="left:124px;top:48px;width:42px;font-size:1.5px;line-height:2px">Lorem ipsum dolor sit amet, consectetuer adipiscing elit. Maecenas porttitor congue massa.</div>
 <div class="foot"><span>website.com</span><i></i><span>Page | 16</span></div>
</section>
<section class="slide c5 r3">
 <div class="title" style="top:8px">Company <b>Leader</b></div>
 <div class="abs" style="left:15px;top:25px;width:150px;display:flex;gap:4px">
  <div class="card" style="position:relative;flex:1;height:55px"><div style="height:11px;background:var(--purple)"></div><div class="pcirc" role="img" aria-label="Portrait photo of team leader" style="left:9px;top:3px;width:17px;height:17px;border:1px solid #fff"></div><div style="margin-top:11px;text-align:center;font-size:1.8px;color:var(--purple);font-weight:600">Lena Brook</div><div class="tiny" style="text-align:center;font-size:1.4px">Manager of Leader</div><div class="tiny" style="font-size:1.4px;line-height:2px;padding:2px">• Identify the lorem ipsum<br>• The dolor lorem with<br>• Sit amet lorem to the<br>• Amet sit dolor identify</div></div>
  <div class="card" style="position:relative;flex:1;height:55px"><div style="height:11px;background:var(--purple)"></div><div class="pcirc" role="img" aria-label="Portrait photo of team leader" style="left:9px;top:3px;width:17px;height:17px;border:1px solid #fff"></div><div style="margin-top:11px;text-align:center;font-size:1.8px;color:var(--purple);font-weight:600">Nora Vale</div><div class="tiny" style="text-align:center;font-size:1.4px">Manager of Leader</div><div class="tiny" style="font-size:1.4px;line-height:2px;padding:2px">• Identify the lorem ipsum<br>• The dolor lorem with<br>• Sit amet lorem to the<br>• Amet sit dolor identify</div></div>
  <div class="card" style="position:relative;flex:1;height:55px"><div style="height:11px;background:var(--purple)"></div><div class="pcirc" role="img" aria-label="Portrait photo of team leader" style="left:9px;top:3px;width:17px;height:17px;border:1px solid #fff"></div><div style="margin-top:11px;text-align:center;font-size:1.8px;color:var(--purple);font-weight:600">Theo Park</div><div class="tiny" style="text-align:center;font-size:1.4px">Manager of Leader</div><div class="tiny" style="font-size:1.4px;line-height:2px;padding:2px">• Identify the lorem ipsum<br>• The dolor lorem with<br>• Sit amet lorem to the<br>• Amet sit dolor identify</div></div>
  <div class="card" style="position:relative;flex:1;height:55px"><div style="height:11px;background:var(--purple)"></div><div class="pcirc" role="img" aria-label="Portrait photo of team leader" style="left:9px;top:3px;width:17px;height:17px;border:1px solid #fff"></div><div style="margin-top:11px;text-align:center;font-size:1.8px;color:var(--purple);font-weight:600">Ivy Lane</div><div class="tiny" style="text-align:center;font-size:1.4px">Manager of Leader</div><div class="tiny" style="font-size:1.4px;line-height:2px;padding:2px">• Identify the lorem ipsum<br>• The dolor lorem with<br>• Sit amet lorem to the<br>• Amet sit dolor identify</div></div>
 </div>
 <div class="foot"><span>website.com</span><i></i><span>Page | 17</span></div>
</section>
<section class="slide c6 r3">
 <div class="title" style="top:9px">Member <b>Team</b></div>
 <div class="abs" style="left:14px;top:24px;width:72px;height:27px;background:var(--purple)"><div class="pcirc" role="img" aria-label="Portrait photo of team member" style="left:4px;top:4px;width:19px;height:19px"></div><div style="position:absolute;left:32px;top:9px;font-size:2.6px;color:var(--yellow);font-weight:600">Mira Stone</div><div style="position:absolute;left:32px;top:14px;font-size:1.5px;color:#ddd">Marketing Manager</div></div>
 <div class="card" style="left:94px;top:24px;width:33px;height:27px;text-align:center"><div class="pcirc" role="img" aria-label="Portrait photo of team member" style="left:10px;top:3px;width:12px;height:12px"></div><div style="margin-top:17px;font-size:1.7px;font-weight:600">Owen <span style="color:var(--yellow)">Reed</span></div></div>
 <div class="card" style="left:132px;top:24px;width:33px;height:27px;text-align:center"><div class="pcirc" role="img" aria-label="Portrait photo of team member" style="left:10px;top:3px;width:12px;height:12px"></div><div style="margin-top:17px;font-size:1.7px;font-weight:600">Ravi <span style="color:var(--yellow)">Cole</span></div></div>
 <div class="card" style="left:14px;top:55px;width:33px;height:27px;text-align:center"><div class="pcirc" role="img" aria-label="Portrait photo of team member" style="left:10px;top:3px;width:12px;height:12px"></div><div style="margin-top:17px;font-size:1.7px;font-weight:600">Dana <span style="color:var(--yellow)">Frost</span></div></div>
 <div class="card" style="left:54px;top:55px;width:33px;height:27px;text-align:center"><div class="pcirc" role="img" aria-label="Portrait photo of team member" style="left:10px;top:3px;width:12px;height:12px"></div><div style="margin-top:17px;font-size:1.7px;font-weight:600">Eli <span style="color:var(--yellow)">Moss</span></div></div>
 <div class="card" style="left:94px;top:55px;width:33px;height:27px;text-align:center"><div class="pcirc" role="img" aria-label="Portrait photo of team member" style="left:10px;top:3px;width:12px;height:12px"></div><div style="margin-top:17px;font-size:1.7px;font-weight:600">Sara <span style="color:var(--yellow)">Quinn</span></div></div>
 <div class="card" style="left:132px;top:55px;width:33px;height:27px;text-align:center"><div class="pcirc" role="img" aria-label="Portrait photo of team member" style="left:10px;top:3px;width:12px;height:12px"></div><div style="margin-top:17px;font-size:1.7px;font-weight:600">Tess <span style="color:var(--yellow)">Ward</span></div></div>
 <div class="foot"><span>website.com</span><i></i><span>Page | 18</span></div>
</section>

<!-- Row 4 -->
<section class="slide c1 r4">
 <div class="t" style="left:8px;top:7px">Presentation <b>List</b></div>
 <svg class="abs" style="left:8px;top:20px" width="162" height="66" font-family="Poppins" font-size="2" text-anchor="middle" fill="#555">
  <line x1="2" y1="30" x2="160" y2="30" stroke="#bbb" stroke-width=".4"/>
  <g fill="#6a2c9c"><circle cx="17" cy="30" r="3"/><circle cx="42" cy="30" r="3"/><circle cx="67" cy="30" r="3"/><circle cx="92" cy="30" r="3"/><circle cx="142" cy="30" r="3"/></g>
  <circle cx="117" cy="30" r="4.5" fill="#f6ad00"/>
  <g fill="#fff" font-size="1.6"><text x="17" y="30.6">2021</text><text x="42" y="30.6">2022</text><text x="67" y="30.6">2023</text><text x="92" y="30.6">2024</text><text x="117" y="30.6">2025</text><text x="142" y="30.6">2026</text></g>
  <text x="42" y="8" fill="#222">Lorem Ipsum</text><text x="92" y="8" fill="#222">Lorem Ipsum</text><text x="142" y="8" fill="#222">Lorem Ipsum</text>
  <text x="42" y="11">consectetuer adipisc.</text><text x="92" y="11">consectetuer adipisc.</text><text x="142" y="11">consectetuer adipisc.</text>
  <text x="17" y="51" fill="#222">Lorem Ipsum</text><text x="67" y="51" fill="#222">Lorem Ipsum</text><text x="117" y="51" fill="#f6ad00">The Goal</text>
  <text x="17" y="54">consectetuer adipisc.</text><text x="67" y="54">consectetuer adipisc.</text><text x="117" y="54">consectetuer adipisc.</text>
 </svg>
 <div class="foot"><span>website.com</span><i></i><span>Page | 19</span></div>
</section>
<section class="slide c2 r4">
 <div class="abs" style="left:11px;top:28px;font-size:5px;font-weight:600;line-height:6px">Circle Graph<br><span style="color:var(--purple)">Analyse</span></div>
 <div class="abs tiny" style="left:11px;top:53px;width:50px;font-size:1.5px;line-height:2px">Lorem ipsum dolor sit amet, consectetuer adipiscing elit. Maecenas porttitor congue massa. Fusce posuere, magna sed pulvinar ultricies.</div>
 <svg class="abs" style="left:70px;top:23px" width="40" height="50" viewBox="0 0 40 50">
  <g fill="none" stroke-width="5"><circle cx="20" cy="20" r="16" stroke="#f6ad00" stroke-dasharray="45 101" transform="rotate(-90 20 20)"/><circle cx="20" cy="20" r="16" stroke="#6a2c9c" stroke-dasharray="0 45 30 101" transform="rotate(-90 20 20)"/><circle cx="20" cy="20" r="16" stroke="#8a55c0" stroke-dasharray="0 75 18 101" transform="rotate(-90 20 20)"/><circle cx="20" cy="20" r="16" stroke="#888" stroke-dasharray="0 93 8 101" transform="rotate(-90 20 20)"/></g>
  <text x="20" y="45" font-size="1.6" text-anchor="middle" fill="#777" font-family="Poppins">■ Jan ■ Feb ■ Mar ■ Apr ■ May ■ Jun</text>
 </svg>
 <div class="card" style="left:125px;top:24px;width:41px;height:19px;padding:2px"><div class="tiny" style="font-size:1.5px">June</div><div style="text-align:right;font-size:5px">$5700</div></div>
 <div class="card" style="left:125px;top:47px;width:41px;height:19px;padding:2px;border:.3px solid var(--yellow)"><div style="font-size:1.5px;color:var(--yellow)">March</div><div style="text-align:right;font-size:5px;color:var(--yellow)">$7600</div></div>
 <div class="foot"><span>website.com</span><i></i><span>Page | 20</span></div>
</section>
<section class="slide c3 r4">
 <div class="title" style="top:11px">Hexa<b>graph</b></div>
 <svg class="abs" style="left:8px;top:32px" width="162" height="50" font-family="Poppins" font-size="2" text-anchor="middle">
  <g fill="#fff" stroke="#ddd" stroke-width=".5">
   <polygon points="17,2 27,7 27,17 17,22 7,17 7,7"/><polygon points="49,2 59,7 59,17 49,22 39,17 39,7"/><polygon points="81,2 91,7 91,17 81,22 71,17 71,7"/><polygon points="113,2 123,7 123,17 113,22 103,17 103,7"/><polygon points="145,2 155,7 155,17 145,22 135,17 135,7"/></g>
  <g fill="#6a2c9c"><text x="17" y="12.7">Step 1</text><text x="49" y="12.7">Step 2</text><text x="81" y="12.7">Step 3</text><text x="113" y="12.7">Step 4</text><text x="145" y="12.7">Step 5</text></g>
  <g fill="#222" font-size="1.8"><text x="17" y="31">Marketing Step</text><text x="49" y="31">Production Step</text><text x="81" y="31">R&amp;D Step</text><text x="113" y="31">Vendor Step</text><text x="145" y="31">Supplier Step</text></g>
  <g fill="#999" font-size="1.5"><text x="17" y="34">Lorem ipsum dolor</text><text x="49" y="34">Lorem ipsum dolor</text><text x="81" y="34">Lorem ipsum dolor</text><text x="113" y="34">Lorem ipsum dolor</text><text x="145" y="34">Lorem ipsum dolor</text><text x="17" y="37">sit amet adipisc</text><text x="49" y="37">sit amet adipisc</text><text x="81" y="37">sit amet adipisc</text><text x="113" y="37">sit amet adipisc</text><text x="145" y="37">sit amet adipisc</text></g>
 </svg>
 <div class="foot"><span>website.com</span><i></i><span>Page | 21</span></div>
</section>
<section class="slide c4 r4">
 <div class="title" style="top:11px">Info<b>graph</b></div>
 <svg class="abs" style="left:15px;top:26px" width="150" height="60" font-family="Poppins" font-size="1.8" text-anchor="middle">
  <g><rect x="5" y="0" width="14" height="20" rx="7" fill="#f6ad00"/><path d="M5 13a7 7 0 0 0 14 0v-3H5z" fill="#6a2c9c"/><text x="12" y="12" fill="#fff">One</text>
  <rect x="44" y="0" width="14" height="20" rx="7" fill="#f6ad00"/><path d="M44 13a7 7 0 0 0 14 0v-3H44z" fill="#6a2c9c"/><text x="51" y="12" fill="#fff">Two</text>
  <rect x="83" y="0" width="14" height="20" rx="7" fill="#f6ad00"/><path d="M83 13a7 7 0 0 0 14 0v-3H83z" fill="#6a2c9c"/><text x="90" y="12" fill="#fff">Three</text>
  <rect x="122" y="0" width="14" height="20" rx="7" fill="#f6ad00"/><path d="M122 13a7 7 0 0 0 14 0v-3h-14z" fill="#6a2c9c"/><text x="129" y="12" fill="#fff">Four</text></g>
  <g fill="#999" font-size="1.5"><text x="12" y="26">Lorem ipsum dolor sit</text><text x="51" y="26">Lorem ipsum dolor sit</text><text x="90" y="26">Lorem ipsum dolor sit</text><text x="129" y="26">Lorem ipsum dolor sit</text><text x="12" y="29">amet consectetuer</text><text x="51" y="29">amet consectetuer</text><text x="90" y="29">amet consectetuer</text><text x="129" y="29">amet consectetuer</text></g>
  <g fill="#f6ad00"><circle cx="12" cy="42" r="4"/><circle cx="51" cy="42" r="4"/><circle cx="90" cy="42" r="4"/><circle cx="129" cy="42" r="4"/></g>
 </svg>
 <div class="foot"><span>website.com</span><i></i><span>Page | 22</span></div>
</section>
<section class="slide c5 r4" style="background:var(--yellow)">
 <div class="title" style="top:11px;color:#fff">Info<b style="color:#fff">graph</b></div>
 <div class="abs" style="left:15px;top:27px;width:150px;display:flex;gap:4px">
  <div style="flex:1;height:54px;background:rgba(255,255,255,.15);padding-top:2px"><svg width="34" height="16"><circle cx="17" cy="8" r="7" fill="#f6ad00" stroke="#fff" stroke-width="1"/><text x="17" y="9.5" font-size="4" fill="#fff" text-anchor="middle" font-family="Poppins">450</text></svg><div style="font-size:1.9px;color:#fff;font-weight:600;padding:3px 3px 0">Step One</div><div style="font-size:1.4px;color:#fff;padding:1px 3px;line-height:2px">Lorem ipsum dolor sit amet consectetuer adipisc.</div></div>
  <div style="flex:1;height:54px;background:rgba(255,255,255,.15);padding-top:2px"><svg width="34" height="16"><circle cx="17" cy="8" r="7" fill="#f6ad00" stroke="#fff" stroke-width="1"/><text x="17" y="9.5" font-size="4" fill="#fff" text-anchor="middle" font-family="Poppins">460</text></svg><div style="font-size:1.9px;color:#fff;font-weight:600;padding:3px 3px 0">Step Two</div><div style="font-size:1.4px;color:#fff;padding:1px 3px;line-height:2px">Lorem ipsum dolor sit amet consectetuer adipisc.</div></div>
  <div style="flex:1;height:54px;background:rgba(255,255,255,.15);padding-top:2px"><svg width="34" height="16"><circle cx="17" cy="8" r="7" fill="#f6ad00" stroke="#fff" stroke-width="1"/><text x="17" y="9.5" font-size="4" fill="#fff" text-anchor="middle" font-family="Poppins">480</text></svg><div style="font-size:1.9px;color:#fff;font-weight:600;padding:3px 3px 0">Step Three</div><div style="font-size:1.4px;color:#fff;padding:1px 3px;line-height:2px">Lorem ipsum dolor sit amet consectetuer adipisc.</div></div>
  <div style="flex:1;height:54px;background:rgba(255,255,255,.15);padding-top:2px"><svg width="34" height="16"><circle cx="17" cy="8" r="7" fill="#f6ad00" stroke="#fff" stroke-width="1"/><text x="17" y="9.5" font-size="4" fill="#fff" text-anchor="middle" font-family="Poppins">490</text></svg><div style="font-size:1.9px;color:#fff;font-weight:600;padding:3px 3px 0">Step Four</div><div style="font-size:1.4px;color:#fff;padding:1px 3px;line-height:2px">Lorem ipsum dolor sit amet consectetuer adipisc.</div></div>
 </div>
 <div class="foot" style="background:#fff;color:#999"><span>website.com</span><i></i><span>Page | 23</span></div>
</section>
<section class="slide c6 r4">
 <div class="title" style="top:11px">Date List <b>Agenda</b></div>
 <div class="abs" style="left:20px;top:31px;width:140px;display:flex;gap:6px;text-align:center">
  <div class="card" style="position:relative;flex:1;height:44px;padding-top:4px"><div style="width:4px;height:4px;border-radius:50%;background:var(--yellow);margin:0 auto"></div><div style="font-size:3px;font-weight:600">23<sup>rd</sup></div><div class="tiny" style="font-size:1.4px;color:var(--purple)">June</div><div class="tiny" style="font-size:1.4px;line-height:2px;text-align:left;padding:3px">• Identify the lorem ipsum<br>• The dolor lorem with<br>• Sit amet lorem to the<br>• The lorem ipsum for dolor</div></div>
  <div class="card" style="position:relative;flex:1;height:44px;padding-top:4px"><div style="width:4px;height:4px;border-radius:50%;background:var(--yellow);margin:0 auto"></div><div style="font-size:3px;font-weight:600">11<sup>st</sup></div><div class="tiny" style="font-size:1.4px;color:var(--purple)">July</div><div class="tiny" style="font-size:1.4px;line-height:2px;text-align:left;padding:3px">• Identify the lorem ipsum<br>• The dolor lorem with<br>• Sit amet lorem to the<br>• The lorem ipsum for dolor</div></div>
  <div class="card" style="position:relative;flex:1;height:44px;padding-top:4px"><div style="width:4px;height:4px;border-radius:50%;background:var(--yellow);margin:0 auto"></div><div style="font-size:3px;font-weight:600">2<sup>nd</sup></div><div class="tiny" style="font-size:1.4px;color:var(--purple)">August</div><div class="tiny" style="font-size:1.4px;line-height:2px;text-align:left;padding:3px">• Identify the lorem ipsum<br>• The dolor lorem with<br>• Sit amet lorem to the<br>• The lorem ipsum for dolor</div></div>
 </div>
 <div class="foot"><span>website.com</span><i></i><span>Page | 24</span></div>
</section>

<!-- Row 5 -->
<section class="slide c1 r5">
 <div class="title" style="top:10px">Monthly <b>Chart</b></div>
 <svg class="abs" style="left:10px;top:28px" width="160" height="58" font-family="Poppins" font-size="1.8" fill="#555">
  <polyline points="9,22 33,12 56,26 90,20 122,24 140,21" fill="none" stroke="#8a55c0" stroke-width=".6"/>
  <g fill="#f6ad00" font-size="2"><text x="6" y="23">45</text><text x="30" y="12">78</text><text x="53" y="28">45</text><text x="87" y="20">48</text><text x="118" y="26">40</text><text x="140" y="21">56</text></g>
  <g font-size="1.6" fill="#333"><text x="9" y="51">JAN</text><text x="33" y="51">FEB</text><text x="56" y="51">MARC</text><text x="78" y="51">APR</text><text x="100" y="51">MAY</text><text x="122" y="51">JUN</text></g>
  <circle cx="142" cy="4" r="3.5" fill="#f6ad00"/><text x="142" y="4.7" fill="#fff" text-anchor="middle" font-size="1.8">49</text>
  <text x="139" y="12" font-size="2.6" fill="#222">May</text><text x="139" y="15" font-size="1.4" fill="#999">Lorem ipsum dolor sit amet</text>
  <circle cx="142" cy="33" r="3.5" fill="#f6ad00"/><text x="142" y="33.7" fill="#fff" text-anchor="middle" font-size="1.8">56</text>
  <text x="139" y="41" font-size="2.6" fill="#222">Jun</text><text x="139" y="44" font-size="1.4" fill="#999">Lorem ipsum dolor sit amet</text>
 </svg>
 <div class="foot"><span>website.com</span><i></i><span>Page | 25</span></div>
</section>
<section class="slide c2 r5">
 <div class="title" style="top:10px">Three Point <b>Value</b></div>
 <svg class="abs" style="left:15px;top:30px" width="80" height="50" font-family="Poppins" text-anchor="middle">
  <path d="M9 12L62 4M9 12L32 29M62 4L32 29" stroke="#8a55c0" stroke-width=".4" fill="none"/>
  <g fill="#f6ad00" stroke="#fff" stroke-width="1"><circle cx="9" cy="12" r="6"/><circle cx="62" cy="4" r="6"/><circle cx="32" cy="29" r="6"/></g>
  <g fill="#6a2c9c" font-size="3"><text x="9" y="12.5">1</text><text x="62" y="4.5">3</text><text x="32" y="29.5">2</text></g>
 </svg>
 <div class="abs" style="left:101px;top:28px;width:65px;font-size:3.4px;line-height:4px">56%<div class="tiny" style="font-size:1.4px;line-height:2px">Lorem ipsum dolor sit amet, consectetuer adipiscing elit.</div><div style="margin-top:3px">76%</div><div class="tiny" style="font-size:1.4px;line-height:2px">Lorem ipsum dolor sit amet, consectetuer adipiscing elit.</div><div style="margin-top:3px">89%</div><div class="tiny" style="font-size:1.4px;line-height:2px">Lorem ipsum dolor sit amet, consectetuer adipiscing elit.</div></div>
 <div class="foot"><span>website.com</span><i></i><span>Page | 26</span></div>
</section>
<section class="slide c3 r5">
 <div class="title" style="top:10px">Chart <b>Infograph</b></div>
 <svg class="abs" style="left:64px;top:34px" width="50" height="48">
  <ellipse cx="25" cy="34" rx="20" ry="9" fill="#3f1d5e"/><path d="M5 26v8a20 9 0 0 0 40 0v-8z" fill="#3f1d5e"/>
  <path d="M25 26L5 26a20 9 0 0 0 24 8.8z" fill="#6a2c9c"/><path d="M25 26l4 8.8a20 9 0 0 0 16-8.8z" fill="#8a55c0"/>
  <path d="M25 20L45 20A20 9 0 0 0 25 11z" fill="#9a6ad0"/><path d="M25 20v-9A20 9 0 0 0 6 17z" fill="#f6ad00"/><path d="M6 17v-4l19-5v3z" fill="#d99500"/>
 </svg>
 <div class="abs" style="left:18px;top:37px;width:40px;text-align:right"><div style="font-size:1.9px;color:var(--yellow);font-weight:600">Analyse One</div><div class="tiny" style="font-size:1.4px;line-height:2px">Lorem ipsum dolor sit amet, consectetuer adipisc.</div><div style="font-size:1.9px;color:var(--yellow);font-weight:600;margin-top:4px">Analyse Two</div><div class="tiny" style="font-size:1.4px;line-height:2px">Lorem ipsum dolor sit amet, consectetuer adipisc.</div></div>
 <div class="abs" style="left:120px;top:37px;width:40px"><div style="font-size:1.9px;color:var(--purple);font-weight:600">Analyse Three</div><div class="tiny" style="font-size:1.4px;line-height:2px">Lorem ipsum dolor sit amet, consectetuer adipisc.</div><div style="font-size:1.9px;color:var(--purple);font-weight:600;margin-top:4px">Analyse Four</div><div class="tiny" style="font-size:1.4px;line-height:2px">Lorem ipsum dolor sit amet, consectetuer adipisc.</div></div>
 <div class="foot"><span>website.com</span><i></i><span>Page | 27</span></div>
</section>
<section class="slide c4 r5">
 <div class="t" style="left:11px;top:9px">Timeline <b>Project</b></div>
 <svg class="abs" style="left:8px;top:30px" width="162" height="40" font-family="Poppins" font-size="1.8">
  <line x1="2" y1="12" x2="160" y2="12" stroke="#ccc" stroke-width=".4"/>
  <circle cx="10" cy="12" r="3.2" fill="#6a2c9c"/><circle cx="50" cy="20" r="3.2" fill="#6a2c9c"/><circle cx="91" cy="12" r="3.6" fill="#f6ad00"/><circle cx="130" cy="20" r="3.2" fill="#6a2c9c"/>
  <g fill="#f6ad00" font-size="2"><text x="58" y="5">April 2023</text><text x="141" y="5">July 2023</text><text x="17" y="19">March 2023</text><text x="98" y="19">June 2023</text></g>
  <g fill="#999" font-size="1.4"><text x="58" y="8">Lorem ipsum dolor sit amet</text><text x="141" y="8">Lorem ipsum dolor sit</text><text x="17" y="22">Lorem ipsum dolor sit amet</text><text x="98" y="22">Lorem ipsum dolor sit amet</text></g>
 </svg>
 <div class="foot"><span>website.com</span><i></i><span>Page | 28</span></div>
</section>
<section class="slide c5 r5">
 <div class="t" style="left:11px;top:9px">Timeline <b>Project</b></div>
 <svg class="abs" style="left:8px;top:26px" width="162" height="44" font-family="Poppins" font-size="1.8">
  <line x1="2" y1="16" x2="160" y2="16" stroke="#ccc" stroke-width=".4"/>
  <circle cx="25" cy="24" r="3.2" fill="#f6ad00"/><circle cx="80" cy="8" r="6" fill="#f6ad00"/><circle cx="137" cy="24" r="3.2" fill="#6a2c9c"/>
  <g fill="#f6ad00" font-size="2"><text x="15" y="8">August 2023</text><text x="122" y="8">October 2023</text><text x="74" y="24">Sept 2023</text></g>
  <g fill="#999" font-size="1.4"><text x="15" y="11">Lorem ipsum dolor sit amet</text><text x="122" y="11">Lorem ipsum dolor sit amet</text><text x="74" y="27">Lorem ipsum dolor sit amet</text></g>
 </svg>
 <div class="foot"><span>website.com</span><i></i><span>Page | 29</span></div>
</section>
<section class="slide c6 r5">
 <div class="title" style="top:9px">Circle <b>Graph</b></div>
 <svg class="abs" style="left:15px;top:27px" width="150" height="50" font-family="Poppins" text-anchor="middle">
  <g fill="none" stroke-width="1.6"><circle cx="24" cy="13" r="11" stroke="#eee"/><circle cx="74" cy="13" r="11" stroke="#eee"/><circle cx="124" cy="13" r="11" stroke="#eee"/>
  <circle cx="24" cy="13" r="11" stroke="#f6ad00" stroke-dasharray="50 69" transform="rotate(-90 24 13)"/><circle cx="74" cy="13" r="11" stroke="#f6ad00" stroke-dasharray="55 69" transform="rotate(-90 74 13)"/><circle cx="124" cy="13" r="11" stroke="#f6ad00" stroke-dasharray="40 69" transform="rotate(-90 124 13)"/></g>
  <g fill="#f6ad00" font-size="5"><text x="24" y="15">72%</text><text x="74" y="15">80%</text><text x="124" y="15">58%</text></g>
  <g fill="#f6ad00" font-size="1.8"><text x="24" y="31">Data One</text><text x="74" y="31">Data Two</text><text x="124" y="31">Data Three</text></g>
  <g fill="#999" font-size="1.4"><text x="24" y="34">Lorem ipsum dolor sit amet</text><text x="74" y="34">Lorem ipsum dolor sit amet</text><text x="124" y="34">Lorem ipsum dolor sit amet</text><text x="24" y="37">consectetuer adipisc</text><text x="74" y="37">consectetuer adipisc</text><text x="124" y="37">consectetuer adipisc</text></g>
 </svg>
 <div class="foot"><span>website.com</span><i></i><span>Page | 30</span></div>
</section>

<!-- Row 6 -->
<section class="slide c1 r6">
 <div class="title" style="top:9px">Profit <b>Chart</b></div>
 <svg class="abs" style="left:12px;top:22px" width="158" height="64" font-family="Poppins" font-size="1.6">
  <rect x="0" y="0" width="118" height="62" fill="#fde9b3"/><rect x="70" y="3" width="10" height="55" fill="#f9cf5f"/>
  <g stroke="#f6ad00" stroke-width=".4"><line x1="16" y1="20" x2="16" y2="56"/><line x1="24" y1="26" x2="24" y2="56"/><line x1="32" y1="16" x2="32" y2="56"/><line x1="40" y1="30" x2="40" y2="56"/><line x1="48" y1="22" x2="48" y2="56"/><line x1="56" y1="34" x2="56" y2="56"/><line x1="64" y1="28" x2="64" y2="56"/><line x1="75" y1="12" x2="75" y2="56"/><line x1="86" y1="24" x2="86" y2="56"/><line x1="94" y1="32" x2="94" y2="56"/><line x1="102" y1="26" x2="102" y2="56"/></g>
  <g stroke="#6a2c9c" stroke-width=".4"><line x1="18" y1="40" x2="18" y2="56"/><line x1="26" y1="36" x2="26" y2="56"/><line x1="34" y1="42" x2="34" y2="56"/><line x1="42" y1="38" x2="42" y2="56"/><line x1="50" y1="44" x2="50" y2="56"/><line x1="58" y1="40" x2="58" y2="56"/><line x1="66" y1="42" x2="66" y2="56"/><line x1="77" y1="36" x2="77" y2="56"/><line x1="88" y1="40" x2="88" y2="56"/><line x1="96" y1="44" x2="96" y2="56"/><line x1="104" y1="40" x2="104" y2="56"/></g>
  <rect x="64" y="4" width="22" height="4" rx="1" fill="#6a2c9c"/><text x="75" y="6.8" fill="#fff" text-anchor="middle">5,323.00 USD</text>
  <g fill="#777"><text x="4" y="10">3K</text><text x="4" y="24">2K</text><text x="4" y="38">1K</text><text x="4" y="52">0</text></g>
  <g fill="#6a2c9c" font-size="2"><text x="124" y="8">01 Analyse</text><text x="124" y="30">06 Analyse</text><text x="124" y="50">12 Analyse</text></g>
  <g fill="#999" font-size="1.3"><text x="124" y="11">Lorem ipsum dolor sit</text><text x="124" y="14">consectetuer adipisc</text><text x="124" y="33">Lorem ipsum dolor sit</text><text x="124" y="36">consectetuer adipisc</text><text x="124" y="53">Lorem ipsum dolor sit</text><text x="124" y="56">consectetuer adipisc</text></g>
 </svg>
 <div class="foot"><span>website.com</span><i></i><span>Page | 31</span></div>
</section>
<section class="slide c2 r6" style="background:var(--yellow)">
 <div class="title" style="top:12px;color:#222">Table <b style="color:var(--purple)">Chart</b></div>
 <svg class="abs" style="left:25px;top:27px" width="128" height="62" font-family="Poppins" font-size="1.6" fill="#fff">
  <rect width="128" height="6" fill="#a74f1e"/>
  <g font-size="1.8"><text x="4" y="4">Data Name</text><text x="36" y="4">Number</text><text x="58" y="4">Profit Rate</text><text x="80" y="4">Option</text><text x="96" y="4">Rate</text><text x="110" y="4">Performance</text></g>
  <g fill="rgba(255,255,255,.18)"><rect y="7" width="128" height="6"/><rect y="21" width="128" height="6"/><rect y="35" width="128" height="6"/><rect y="49" width="128" height="6"/></g>
  <g fill="#f0c24f"><rect y="14" width="128" height="6"/><rect y="28" width="128" height="6"/><rect y="42" width="128" height="6"/></g>
  <g fill="#fff" opacity=".85"><text x="4" y="11">Data One</text><text x="4" y="18">Data Two</text><text x="4" y="25">Data Three</text><text x="4" y="32">Data Four</text><text x="4" y="39">Data Five</text><text x="4" y="46">Data Six</text>
  <text x="36" y="11">3,897</text><text x="36" y="18">4,3444</text><text x="36" y="25">14,232</text><text x="36" y="32">3,891</text><text x="36" y="39">4,234</text><text x="36" y="46">6,890</text>
  <text x="60" y="11">23.5</text><text x="60" y="18">34.3</text><text x="60" y="25">22.7</text><text x="60" y="32">5.23</text><text x="60" y="39">90</text><text x="60" y="46">50</text>
  <text x="82" y="11">Yes</text><text x="82" y="18">No</text><text x="82" y="25">Yes</text><text x="82" y="32">No</text><text x="82" y="39">Yes</text><text x="82" y="46">No</text>
  <text x="97" y="11">70</text><text x="97" y="18">81</text><text x="97" y="25">77</text><text x="97" y="32">89</text><text x="97" y="39">92</text><text x="97" y="46">87</text>
  <text x="112" y="11">3,290</text><text x="112" y="18">3,291</text><text x="112" y="25">3,887</text><text x="112" y="32">57,000</text><text x="112" y="39">5,444</text><text x="112" y="46">56.7</text></g>
 </svg>
 <div class="foot" style="background:#fff;color:#999"><span>website.com</span><i></i><span>Page | 32</span></div>
</section>
<section class="slide c3 r6">
 <div class="title" style="top:9px">KPI <b>Dashboard</b></div>
 <svg class="abs" style="left:10px;top:24px" width="160" height="62" font-family="Poppins" font-size="1.8" fill="#333">
  <g fill="#6a2c9c" font-size="1.9"><text x="15" y="3">Project Done</text><text x="55" y="3">Monthly Earning</text><text x="97" y="3">Costumer Acc</text><text x="139" y="3">Claim</text></g>
  <g fill="#999" font-size="2.2"><text x="18" y="7">563</text><text x="60" y="7">$32,470</text><text x="102" y="7">3,877</text><text x="142" y="7">0</text></g>
  <g stroke="#eee" stroke-width=".3"><line x1="0" y1="10" x2="160" y2="10"/></g>
  <text x="2" y="16" font-size="1.6">5 Active Dashboard</text><text x="56" y="16" font-size="1.6">2 User Per Role</text><text x="108" y="16" font-size="1.6"># Live Profit and Net</text>
  <g font-size="1.4" fill="#777"><text x="4" y="27">Data Five</text><text x="4" y="31">Data Four</text><text x="4" y="35">Data Three</text><text x="4" y="39">Data Two</text><text x="4" y="43">Data One</text></g>
  <rect x="16" y="26" width="6" height="1.6" fill="#6a2c9c"/><rect x="16" y="30" width="9" height="1.6" fill="#6a2c9c"/><rect x="16" y="34" width="15" height="1.6" fill="#f6ad00"/><rect x="16" y="38" width="17" height="1.6" fill="#888"/><rect x="16" y="42" width="20" height="1.6" fill="#f6ad00"/>
  <g fill="none" stroke-width="2.5"><circle cx="72" cy="36" r="8" stroke="#f6ad00"/><circle cx="72" cy="36" r="8" stroke="#6a2c9c" stroke-dasharray="18 50"/></g>
  <text x="112" y="24" font-size="1.8">Net Profit &amp; Net sales</text><text x="118" y="33" font-size="1.8">Net profit</text><text x="115" y="38" font-size="3" fill="#6a2c9c">$44,587M</text><text x="114" y="43" font-size="1.8">Net sales = $15M</text>
 </svg>
 <div class="foot"><span>website.com</span><i></i><span>Page | 33</span></div>
</section>
<section class="slide c4 r6">
 <div class="title" style="top:9px">KPI <b>Dashboard</b></div>
 <svg class="abs" style="left:10px;top:23px" width="160" height="64" font-family="Poppins" font-size="1.5" fill="#555">
  <text x="2" y="3">Data Statistics</text><text x="128" y="3">Costumer Email</text>
  <g fill="#f6ad00"><rect x="22" y="16" width="2" height="10"/><rect x="30" y="12" width="2" height="14"/><rect x="38" y="10" width="2" height="16"/><rect x="46" y="14" width="2" height="12"/><rect x="54" y="11" width="2" height="15"/><rect x="62" y="15" width="2" height="11"/><rect x="70" y="12" width="2" height="14"/><rect x="78" y="16" width="2" height="10"/><rect x="86" y="13" width="2" height="13"/><rect x="94" y="11" width="2" height="15"/><rect x="102" y="14" width="2" height="12"/><rect x="110" y="9" width="2" height="17"/></g>
  <g fill="none" stroke="#f6ad00" stroke-width="1"><circle cx="140" cy="15" r="7"/></g>
  <g fill="#fef0c9"><path d="M4 60l6-6 4 3 6-7 6 4 4-5v11z"/><path d="M40 60l6-6 4 3 6-7 6 4 4-5v11z"/><path d="M76 60l6-6 4 3 6-7 6 4 4-5v11z"/></g><path d="M112 60l6-6 4 3 6-7 6 4 4-5v11z" fill="#fdd9d9"/>
  <g font-size="1.6" fill="#222"><text x="8" y="41">Sales</text><text x="44" y="41">Revenue</text><text x="80" y="41">Clients</text><text x="116" y="41">Trade</text></g>
  <g font-size="1.5"><text x="8" y="44">$7,620</text><text x="44" y="44">$4,280</text><text x="80" y="44">$5,290</text><text x="116" y="44">$7,780</text></g>
 </svg>
 <div class="foot"><span>website.com</span><i></i><span>Page | 34</span></div>
</section>
<section class="slide c5 r6">
 <div class="title" style="top:9px">Dash<b style="color:var(--ink)">board</b></div>
 <svg class="abs" style="left:10px;top:22px" width="160" height="64" font-family="Poppins" font-size="1.4" fill="#555">
  <text x="2" y="3">Net Profit Margin</text><text x="120" y="3">Rate Profitability Indicator</text>
  <g fill="#6a2c9c"><circle cx="16" cy="10" r=".8"/><circle cx="28" cy="12" r=".8"/><circle cx="40" cy="9" r=".8"/><circle cx="52" cy="13" r=".8"/><circle cx="64" cy="11" r=".8"/><circle cx="76" cy="10" r=".8"/><circle cx="88" cy="12" r=".8"/><circle cx="100" cy="9" r=".8"/></g>
  <g fill="#f6ad00"><circle cx="16" cy="15" r=".8"/><circle cx="28" cy="17" r=".8"/><circle cx="40" cy="14" r=".8"/><circle cx="52" cy="18" r=".8"/><circle cx="64" cy="16" r=".8"/><circle cx="76" cy="15" r=".8"/><circle cx="88" cy="17" r=".8"/><circle cx="100" cy="14" r=".8"/></g>
  <g fill="#f6ad00"><rect x="136" y="5" width="6" height="1.5"/><rect x="136" y="10" width="10" height="1.5"/><rect x="136" y="15" width="4" height="1.5"/><rect x="136" y="20" width="12" height="1.5"/></g>
  <text x="2" y="31">Past Year vs Target vs Actual</text>
  <path d="M4 48L20 44 40 40 60 38 80 36 100 40 110 42" fill="none" stroke="#f6ad00" stroke-width=".5"/>
  <g fill="#f6ad00"><rect x="8" y="48" width="2" height="10"/><rect x="18" y="46" width="2" height="12"/><rect x="28" y="44" width="2" height="14"/><rect x="38" y="47" width="2" height="11"/><rect x="48" y="45" width="2" height="13"/><rect x="58" y="43" width="2" height="15"/><rect x="68" y="46" width="2" height="12"/><rect x="78" y="44" width="2" height="14"/><rect x="88" y="42" width="2" height="16"/><rect x="98" y="45" width="2" height="13"/></g>
  <g fill="#6a2c9c"><rect x="11" y="52" width="1.5" height="6"/><rect x="21" y="50" width="1.5" height="8"/><rect x="31" y="52" width="1.5" height="6"/><rect x="41" y="51" width="1.5" height="7"/><rect x="51" y="50" width="1.5" height="8"/><rect x="61" y="52" width="1.5" height="6"/><rect x="71" y="51" width="1.5" height="7"/><rect x="81" y="50" width="1.5" height="8"/><rect x="91" y="52" width="1.5" height="6"/><rect x="101" y="51" width="1.5" height="7"/></g>
  <rect x="116" y="34" width="40" height="24" fill="#fff" stroke="#eee" stroke-width=".3"/><circle cx="121" cy="39" r="1.5" fill="#f6ad00"/><text x="124" y="40" font-size="2.2" fill="#222">68.780.930</text><text x="119" y="45">Lorem ipsum is simply</text><text x="119" y="48">dummy text of the</text>
 </svg>
 <div class="foot"><span>website.com</span><i></i><span>Page | 35</span></div>
</section>
<section class="slide c6 r6">
 <div class="title" style="top:9px">KPI <b>Dashboard</b></div>
 <svg class="abs" style="left:10px;top:22px" width="160" height="64" font-family="Poppins" font-size="1.4" fill="#999">
  <g><text x="40" y="3">May</text><text x="53" y="3">Jun</text><text x="66" y="3">Jul</text><text x="79" y="3">Aug</text><text x="92" y="3">Sep</text><text x="105" y="3">Oct</text><text x="118" y="3">Nov</text><text x="131" y="3">Dec</text><text x="144" y="3">Jan</text></g>
  <circle cx="4" cy="11" r="1.4" fill="#f6ad00"/><text x="8" y="11.5">Team One</text>
  <circle cx="4" cy="28" r="1.4" fill="#6a2c9c"/><text x="8" y="28.5">Team Two</text>
  <circle cx="4" cy="45" r="1.4" fill="#888"/><text x="8" y="45.5">Team Three</text>
  <rect x="52" y="10" width="20" height="3.5" rx="1.7" fill="#f6ad00"/><rect x="82" y="10" width="58" height="3.5" rx="1.7" fill="#6b7380"/>
  <rect x="68" y="21" width="44" height="3.5" rx="1.7" fill="#6a2c9c"/><rect x="56" y="28" width="18" height="3.5" rx="1.7" fill="#6b7380"/><rect x="90" y="28" width="36" height="3.5" rx="1.7" fill="#f6ad00"/>
  <rect x="60" y="43" width="56" height="3.5" rx="1.7" fill="#f6ad00"/><rect x="128" y="43" width="20" height="3.5" rx="1.7" fill="#6a2c9c"/>
  <g><text x="40" y="60">2022</text><text x="53" y="60">2022</text><text x="66" y="60">2022</text><text x="79" y="60">2022</text><text x="92" y="60">2022</text><text x="105" y="60">2022</text><text x="118" y="60">2022</text><text x="131" y="60">2022</text><text x="144" y="60">2023</text></g>
 </svg>
 <div class="foot"><span>website.com</span><i></i><span>Page | 36</span></div>
</section>

<!-- Row 7 -->
<section class="slide c1 r7">
 <div class="title" style="top:9px">Get In <b>Touch</b></div>
 <div class="abs" style="left:17px;top:26px;font-size:3.2px;line-height:4px">Our Professional &amp; Qualified<br>Customer Service <span style="color:var(--purple)">Available 24/7</span></div>
 <div class="abs" style="left:17px;top:59px;font-size:2px;line-height:2.6px">Our Address<div class="tiny" style="font-size:1.5px;line-height:2.1px">12 Harbor Lane,<br>Easton City</div></div>
 <div class="card" style="left:50px;top:55px;width:32px;height:19px;padding:3px;font-size:2px">Phone &amp; Email<div class="tiny" style="font-size:1.5px;line-height:2.1px">+00 555 0100<br>hello@brightpath.co</div></div>
 <div class="abs" style="left:108px;top:27px;font-size:1.8px;line-height:14px;color:#555">
  <div style="display:flex;align-items:center;gap:6px"><span style="width:5px;height:5px;background:var(--purple)"></span>facebook/BrightPath.co</div>
  <div style="display:flex;align-items:center;gap:6px"><span style="width:5px;height:5px;background:var(--purple)"></span>instagram/BrightPath.co</div>
  <div style="display:flex;align-items:center;gap:6px"><span style="width:5px;height:5px;background:var(--purple)"></span>twitter/BrightPath.co</div>
  <div style="display:flex;align-items:center;gap:6px"><span style="width:5px;height:5px;background:var(--purple)"></span>linkedin/BrightPath.co</div>
 </div>
 <div class="foot"><span>website.com</span><i></i><span>Page | 37</span></div>
</section>
<section class="slide c2 r7" style="background:var(--purple)">
 <div class="abs" style="left:0;right:0;top:30px;text-align:center;font-size:10px;font-weight:600;color:var(--yellow)">Thank You</div>
 <div class="abs" style="left:69px;top:45px;width:40px;height:.5px;background:var(--yellow)"></div>
 <div class="abs" style="left:45px;top:50px;width:88px;text-align:center;font-size:1.7px;line-height:2.4px;color:#ddd">Lorem ipsum dolor sit amet, consectetuer adipiscing elit. Maecenas porttitor congue massa. Fusce posuere, magna sed pulvinar ultricies.</div>
 <div class="abs" style="left:71px;top:63px;display:flex;gap:10px"><span style="width:5px;height:5px;border:.4px solid #fff;border-radius:50%"></span><span style="width:5px;height:5px;border:.4px solid #fff;border-radius:50%"></span><span style="width:5px;height:5px;border:.4px solid #fff;border-radius:50%"></span></div>
</section>
<section class="slide c3 r7">
 <svg class="icons" role="img" aria-label="Grid of business line icons" width="162" height="82"><defs><pattern id="ic1" width="10.8" height="16.4" patternUnits="userSpaceOnUse"><rect x="2.5" y="5" width="4" height="4" rx="1" fill="none" stroke="#666" stroke-width=".6"/><rect x="3.7" y="6.2" width="1.6" height="1.6" fill="#666"/></pattern></defs><rect width="162" height="82" fill="url(#ic1)"/></svg>
</section>
<section class="slide c4 r7">
 <svg class="icons" role="img" aria-label="Grid of business line icons" width="162" height="82"><defs><pattern id="ic2" width="10.8" height="16.4" patternUnits="userSpaceOnUse"><circle cx="5" cy="7" r="2.3" fill="none" stroke="#666" stroke-width=".6"/><path d="M4 7h2" stroke="#666" stroke-width=".6"/></pattern></defs><rect width="162" height="82" fill="url(#ic2)"/></svg>
</section>
<section class="slide c5 r7">
 <svg class="icons" role="img" aria-label="Grid of business line icons" width="162" height="82"><defs><pattern id="ic3" width="10.8" height="16.4" patternUnits="userSpaceOnUse"><path d="M3 9h4M3.5 9V6.5h1v2.5M5.5 9V5h1v4" fill="none" stroke="#666" stroke-width=".6"/></pattern></defs><rect width="162" height="82" fill="url(#ic3)"/></svg>
</section>
<section class="slide c6 r7">
 <svg class="icons" role="img" aria-label="Grid of business line icons" width="162" height="82"><defs><pattern id="ic4" width="10.8" height="16.4" patternUnits="userSpaceOnUse"><path d="M5 4.8l2 3.6H3z" fill="none" stroke="#666" stroke-width=".6"/><circle cx="5" cy="9.2" r=".7" fill="#666"/></pattern></defs><rect width="162" height="82" fill="url(#ic4)"/></svg>
</section>

</body></html>
```